依頼詳細
屋外にタペストリーで掲げている店案内ですが、ショッピングセンター内にあるため屋外からエステだと一目でわかるものにしたいと考えております。そのためのデザインをお願いいたします。
記載項目
記載項目
特にエステティックであることをはっきりと掲載したいため「ロゴマーク」「エステティックサロン」「美顔」「痩身」「脱毛」というワードを大きく
続いて「電話番号」「営業時間」
また「店名」も掲載しますが目立たなくとも良いです。
ロゴマークは添付のものをご利用ください。
色ならびにロゴマーク中のグラデーションの変更はしないようにお願いいたします。
参考として旧タペストリーと他店の駐車場看板を添付します。
旧タペストリーのデザインとは全くかけ離れて構いません。
駐車場看板は見せ方の参考として添付します。店名よりもエステティックを強調しているという事の参考になればと思います。

店名 ルフィナ花野店
電話番号 0000-00-0000
営業時間 9:30~20:30
サイズ:縦2400mm×横3200mm
希望イメージ
シンプル 複雑
単色 カラフル
暗い 明るい
日常 高級
遊び心 厳粛
未来的 伝統的
女性的 男性的
希望する色
設定なし
納品ファイル
• イラストレーター形式 (.ai)
• フォトショップ形式 (.psd)
補足説明
写真利用の場合は、納品の際は埋め込みではなくリンクでお願いします。
表記につきまして若干変更をさせていただきます、

「エステティックサロン」は英字よりカナ表記が目立つようにお願いいたします。
「美顔」→「フェイシャル」に変更(カナ表記)
「痩身」→「ボディ」に変更(カナ表記)
「脱毛」→変更なし

また女性の画像等はイメージやパーツとして使用いただいてもOKですが、スワンのマークをもう少し前面に出していただけたらと思います。
画像のイメージが前面にでるより、スワンのロゴが前面にでるようにできればと思います。イメージ画像等は全くないものでも可です。

添付でスワンのロゴのみのaiを追加いたします。

締め切りを変更させていただきます。

当方が伝えたいものが、しっかりと出ていて、色味も落ち着きがありながらロゴがはっきりと見えるデザインで好感が持てました。

本当にたくさんのデザインを頂きありがとうございます。

```html
<!DOCTYPE html>
<html lang="ja">
<head>
<meta charset="utf-8">
<title>Esthetic salon RUFINA</title>
<link rel="stylesheet" href="https://fonts.googleapis.com/css2?family=Cinzel:wght@400;500&family=Marcellus&family=Noto+Serif+JP:wght@400;500;600&display=swap">
<style>
  :root {
    --rose: #d9455f;
    --gold: #a9834a;
    --ink: #333333;
    --paper: #ffffff;
    --skin-light: #f6e4d8;
    --skin-mid: #e8c3ab;
    --ornament: #e4e4e4;
  }
  * { margin: 0; padding: 0; box-sizing: border-box; }
  html, body {
    width: 1200px; height: 848px; overflow: hidden;
    background: var(--paper);
  }
  .banner {
    position: absolute; left: 120px; top: 66px;
    width: 960px; height: 720px;
    border: 1px solid var(--ink);
    background: var(--paper);
    overflow: hidden;
  }
  .hero-photo {
    position: absolute; left: 0; top: 0; width: 650px; height: 400px;
    background: radial-gradient(ellipse at 35% 45%, var(--skin-mid) 0%, var(--skin-light) 45%, rgba(255,255,255,0) 75%);
  }
  .ornament {
    position: absolute; left: 564px; top: 30px; width: 396px; height: 690px;
    background: linear-gradient(160deg, rgba(255,255,255,0) 10%, var(--ornament) 55%, rgba(255,255,255,0) 95%);
    opacity: .8;
  }
  .ribbon {
    position: absolute; left: 0; top: 324px; width: 600px; height: 70px;
  }
  .ribbon svg { position: absolute; inset: 0; }
  .ribbon-text {
    position: absolute; left: 0; top: 0; width: 566px; height: 70px;
    display: flex; align-items: center; justify-content: center;
    font-family: "Noto Serif JP", serif; font-weight: 500;
    font-size: 44px; color: var(--paper); letter-spacing: 1px;
  }
  .brand-mark {
    position: absolute; left: 84px; top: 436px; width: 96px; height: 96px;
    border-radius: 50%; background: var(--rose);
  }
  .brand-tag {
    position: absolute; left: 204px; top: 456px;
    font-family: "Marcellus", serif; font-size: 25px; color: var(--rose);
    line-height: 1;
  }
  .brand-name {
    position: absolute; left: 200px; top: 488px;
    font-family: "Marcellus", serif; font-size: 82px;
    color: var(--rose); letter-spacing: 2px; line-height: 1;
  }
  .branch {
    position: absolute; left: 204px; top: 562px; width: 290px;
    display: flex; align-items: center; gap: 8px;
    font-family: "Noto Serif JP", serif; font-size: 13px; color: var(--gold);
  }
  .branch::before, .branch::after {
    content: ""; flex: 1; height: 1px; background: var(--gold);
  }
  .info {
    position: absolute; left: 70px; width: 440px; text-align: center;
    font-family: "Cinzel", serif; font-size: 24px; line-height: 1;
    color: var(--rose); letter-spacing: 4px; white-space: nowrap;
  }
  .info.hours { top: 608px; }
  .info.hours .gap { display: inline-block; width: 34px; }
  .info.tel { top: 648px; }
  .menu-item {
    position: absolute; left: 668px; width: 200px; text-align: center;
  }
  .menu-kanji {
    font-family: "Noto Serif JP", serif; font-weight: 600;
    color: var(--gold); line-height: 1; white-space: nowrap;
  }
  .menu-kanji .lead { font-size: 100px; }
  .menu-kanji .follow { font-size: 74px; }
  .menu-label {
    margin-top: 22px;
    font-family: "Cinzel", serif; font-size: 18px; line-height: 1;
    color: var(--rose); letter-spacing: 2px;
  }
  .menu-item.facial { top: 66px; }
  .menu-item.removal { top: 278px; }
  .menu-item.slimming { top: 496px; }
</style>
</head>
<body>
  <main class="banner">
    <div class="hero-photo" role="img" aria-label="女性が腕を肩にのせ目を閉じている美容イメージ写真"></div>
    <div class="ornament" role="img" aria-label="淡いグレーの植物模様と蝶の装飾"></div>

    <div class="ribbon">
      <svg width="600" height="70" viewBox="0 0 600 70">
        <polygon points="0,0 600,0 568,35 600,70 0,70" fill="var(--rose)"/>
      </svg>
      <div class="ribbon-text">エステティックサロン</div>
    </div>

    <div class="brand-mark"></div>
    <div class="brand-tag">Esthetic salon</div>
    <div class="brand-name">RUFINA</div>
    <div class="branch">ルフィナ花野店</div>

    <p class="info hours">OPEN 9:30<span class="gap"></span>CLOSE 20:30</p>
    <p class="info tel">TEL.0000-00-0000</p>

    <section class="menu-item facial">
      <div class="menu-kanji"><span class="lead">美</span><span class="follow">顔</span></div>
      <div class="menu-label">FACIAL</div>
    </section>
    <section class="menu-item removal">
      <div class="menu-kanji"><span class="lead">脱</span><span class="follow">毛</span></div>
      <div class="menu-label">REMOVAL</div>
    </section>
    <section class="menu-item slimming">
      <div class="menu-kanji"><span class="lead">痩</span><span class="follow">身</span></div>
      <div class="menu-label">SLIMMING</div>
    </section>
  </main>
</body>
</html>
```